Recipe mobile app, new flow and design for uploading recipe process

I need a new recipe upload process that's simple, intuitive, and engaging.
The goal is to have a user-friendly and fast flow.
The app is a social recipe library where anyone can upload a recipe after signing up. I currently have a flow, but it's "boring," so I'd like to significantly improve this aspect of the app.
When I create a new recipe, it's immediately saved and labeled as a draft. I'll then need to specify:
- Recipe title
- Cover image (required)
- Number of people (how many people is the recipe for)
- Ingredients (name, quantity, and unit of measurement)
- Recipe explanation (broken down into steps, and I can optionally attach an image to each step)
- Upload
Every change is immediately saved, so you can edit, exit, and resume editing later.
I've attached images of the app and the current upload process.
Thank you.
Low design quality
Good morning everyone,
some of the designs received are fantastic, but please make sure to carefully read the requirement so as not to do extra work.
The requirement is to redesign the flow that a user follows when uploading a recipe to the platform.
We have uploaded the current app screens to give you an idea of what the product looks like, what the colors and style are, but we don’t need a full redesign - only the part mentioned above, while keeping the existing style and colors (we cannot rework the entire theme).
To clarify: if you look at the screens shared in the zip file attached to the project, the focus should be on the screens from 5_.png to 10_.png.
These screens can be redesigned in the most creative way you think, as long as the overall theme remains unchanged.
Thank you for your attention.

```html
<!DOCTYPE html>
<html lang="en">
<head>
<meta charset="utf-8">
<title>Recipe Upload Flow</title>
<link rel="stylesheet" href="https://fonts.googleapis.com/css2?family=Inter:wght@400;500;600;700;800&display=swap">
<style>
:root{
  --bg:#dadada;
  --white:#ffffff;
  --ink:#1e222b;
  --muted:#5d6370;
  --soft:#9aa0ab;
  --line:#e3e6ec;
  --grad-a:#667eea;
  --grad-b:#764ba2;
  --blue:#2f6fe8;
  --blue-bg:#eef5ff;
  --blue-line:#cfe0fb;
  --green:#22c55e;
  --green-bg:#effcf4;
  --green-line:#c9f0d6;
  --orange:#f5642c;
  --red:#ef4444;
  --pink:#ec4899;
  --purple:#9b3fd6;
  --purple-bg:#faf3ff;
  --yellow-bg:#fffaeb;
  --yellow-line:#f8e7b0;
  --amber:#b45309;
  --btn-grey:#f2f3f5;
}
*{box-sizing:border-box;margin:0;padding:0}
html,body{width:1200px;height:947px;overflow:hidden;background:var(--bg);font-family:'Inter',sans-serif;color:var(--ink)}
.stage{position:absolute;left:0;top:0;width:2165px;height:1708px;transform:scale(.5543);transform-origin:0 0}
.screen{position:absolute;top:122px;width:305px;background:var(--white);border-radius:34px;overflow:hidden}
.hdr{position:absolute;left:0;top:0;width:100%;height:72px;background:linear-gradient(90deg,var(--grad-a),var(--grad-b))}
.track{position:absolute;left:0;right:0;top:25px;height:4px;background:rgba(255,255,255,.3);border-radius:2px}
.track i{display:block;height:100%;background:var(--white);border-radius:2px}
.step-label{position:absolute;top:44px;width:100%;text-align:center;color:#fff;font-size:10px;font-weight:500}
.abs{position:absolute}
.icon-circle{position:absolute;left:50%;width:66px;height:66px;margin-left:-33px;border-radius:50%;display:flex;align-items:center;justify-content:center;box-shadow:0 6px 14px rgba(0,0,0,.12)}
.title{position:absolute;left:0;width:100%;text-align:center;font-size:20px;font-weight:700}
.sub{position:absolute;left:16px;right:16px;text-align:center;font-size:13px;line-height:20px;color:var(--muted)}
.tip{position:absolute;left:16px;right:16px;border-radius:10px;padding:10px 12px 10px 34px;font-size:9.5px;line-height:13px}
.tip b{display:block;font-size:11.5px;font-weight:600;margin-bottom:3px}
.tip svg{position:absolute;left:12px;top:14px}
.tip.blue{background:var(--blue-bg);border:1px solid var(--blue-line);color:var(--blue)}
.tip.blue b{color:#1d3f8a}
.tip.purple{background:var(--purple-bg);border:1px solid #eedcfb;color:var(--purple)}
.btn{position:absolute;height:49px;border-radius:10px;display:flex;align-items:center;justify-content:center;gap:8px;font-size:15px;font-weight:600}
.btn.primary{background:linear-gradient(90deg,var(--grad-a),var(--grad-b));color:#fff;box-shadow:0 4px 10px rgba(102,126,234,.3)}
.btn.ghost{background:var(--btn-grey);color:#4b5160}
.divider{position:absolute;left:0;right:0;height:1px;background:var(--line)}
.note{position:absolute;left:16px;right:16px;border-radius:10px;text-align:center;font-size:12px;color:#444b57}
.note.yellow{background:var(--yellow-bg);border:1px solid var(--yellow-line)}
.note.green{background:var(--green-bg);border:1px solid var(--green-line)}
.note svg{display:block;margin:14px auto 8px}
.hi-orange{color:#ea580c;font-weight:700}
.hi-green{color:#16a34a;font-weight:700}
.input{position:absolute;border:1.5px solid var(--line);border-radius:8px;font-size:12px;padding:0 10px;display:flex;align-items:center;background:#fff}
.card{position:absolute;left:16px;right:16px;border:1.5px solid var(--line);border-radius:10px;background:#fff}
.num{position:absolute;width:26px;height:26px;border-radius:50%;color:#fff;font-size:11px;font-weight:700;display:flex;align-items:center;justify-content:center}
.photo-slot{position:absolute;border:1.5px dashed #cfd3da;border-radius:8px;text-align:center;color:#7a808c;font-size:12px;line-height:17px}
.photo-slot small{display:block;font-size:10px;line-height:14px;color:#9aa0ab;margin-top:4px}
.chip{position:absolute;border:1.5px solid var(--line);border-radius:10px;background:#fff;font-size:10.5px;font-weight:600;color:#444b57}
.media{position:absolute}
</style>
</head>
<body>
<div class="stage">

<!-- Screen 1: recipe name -->
<section class="screen" style="left:128px;height:668px">
  <div class="hdr" style="height:78px">
    <svg class="abs" style="left:16px;top:22px" width="14" height="14" viewBox="0 0 14 14"><path d="M13 7H2M7 2L2 7l5 5" stroke="#fff" stroke-width="1.8" fill="none" stroke-linecap="round" stroke-linejoin="round"/></svg>
    <div class="track" style="top:59px;left:10px;right:12px"><i style="width:17%"></i></div>
  </div>
  <div class="icon-circle" style="top:96px;background:linear-gradient(135deg,#f97316,#ef4444)">
    <svg width="22" height="22" viewBox="0 0 22 22" fill="#fff"><path d="M5 2h1.4v6H8V2h1.4v6H11V2h1.2v7a3 3 0 01-2.4 2.9V20H7.4v-8.1A3 3 0 015 9z"/><path d="M14.5 2c2 0 3 2.5 3 6v4h-1.6V20h-2.2V2z"/></svg>
  </div>
  <h1 class="title" style="top:174px">What's cooking?</h1>
  <p class="sub" style="top:206px">Give your recipe a catchy name that makes people want to try it!</p>
  <div class="abs" style="left:16px;top:272px;font-size:11.5px;font-weight:500">Recipe Name</div>
  <div class="input" style="left:16px;right:18px;top:294px;height:50px;font-size:14px;color:var(--soft);padding-left:14px;white-space:nowrap;overflow:hidden">e.g., Grandma's Secret Chocolate C</div>
  <div class="tip blue" style="top:358px;height:66px">
    <svg width="12" height="14" viewBox="0 0 12 14"><circle cx="6" cy="5" r="4.5" fill="#3b82f6"/><rect x="4" y="10" width="4" height="3" rx="1" fill="#3b82f6"/></svg>
    <b>Pro Tip</b>Use descriptive words like "crispy," "creamy," or "spicy" to make your recipe more appealing!
  </div>
  <div class="divider" style="top:586px"></div>
  <div class="btn primary" style="left:16px;right:18px;top:607px;height:48px">Continue
    <svg width="14" height="12" viewBox="0 0 14 12"><path d="M1 6h11M7.5 1.5L12 6l-4.5 4.5" stroke="#fff" stroke-width="1.8" fill="none" stroke-linecap="round" stroke-linejoin="round"/></svg></div>
</section>

<!-- Screen 2: cover photo -->
<section class="screen" style="left:506px;height:748px">
  <div class="hdr"><div class="track"><i style="width:33%"></i></div><div class="step-label">Step 2 of 6</div></div>
  <div class="icon-circle" style="top:94px;background:linear-gradient(135deg,#ec4899,#a855f7)">
    <svg width="20" height="18" viewBox="0 0 20 18"><path d="M2 5h4l1.6-2.5h4.8L14 5h4v11H2z" fill="#fff"/><circle cx="10" cy="10" r="3.2" fill="#c65cd4"/></svg>
  </div>
  <h1 class="title" style="top:174px">Picture Perfect</h1>
  <p class="sub" style="top:207px;left:8px;right:8px">A mouth-watering photo makes your recipe irresistible!</p>
  <div class="media" role="img" aria-label="Cover photo of a glazed meat and vegetable dish on a plate" style="left:8px;right:16px;top:276px;height:216px;border-radius:10px;border:1.5px dashed #cfd3da;background:linear-gradient(135deg,#8a6a4a 0%,#c7732f 40%,#6b3a1f 70%,#d8c9b3 100%)"></div>
  <div class="abs" style="right:30px;top:292px;width:24px;height:24px;border-radius:50%;background:#fff;display:flex;align-items:center;justify-content:center">
    <svg width="11" height="11" viewBox="0 0 11 11"><path d="M2 9l.5-2.5L8 1l2 2-5.5 5.5z" fill="none" stroke="#444" stroke-width="1.2"/></svg></div>
  <div class="btn" style="left:8px;top:514px;width:87px;height:70px;flex-direction:column;gap:6px;background:#2f74ea;color:#fff;font-size:10px">
    <svg width="16" height="14" viewBox="0 0 20 18"><path d="M2 5h4l1.6-2.5h4.8L14 5h4v11H2z" fill="#fff"/><circle cx="10" cy="10" r="3" fill="#2f74ea"/></svg>Camera</div>
  <div class="btn" style="left:105px;top:514px;width:87px;height:70px;flex-direction:column;gap:6px;background:#22b55a;color:#fff;font-size:10px">
    <svg width="18" height="14" viewBox="0 0 18 14"><rect x="3" y="1" width="14" height="10" rx="1.5" fill="none" stroke="#fff" stroke-width="1.5"/><path d="M1 4v9h13" fill="none" stroke="#fff" stroke-width="1.5"/><path d="M5 9l3-3 2 2 2-2 3 3" fill="none" stroke="#fff" stroke-width="1.3"/></svg>Gallery</div>
  <div class="btn" style="left:202px;top:514px;width:87px;height:70px;flex-direction:column;gap:6px;background:#9a3fe0;color:#fff;font-size:10px">
    <svg width="16" height="16" viewBox="0 0 16 16"><circle cx="6.5" cy="6.5" r="5" fill="none" stroke="#fff" stroke-width="1.8"/><path d="M10.5 10.5L15 15" stroke="#fff" stroke-width="1.8"/></svg>Search</div>
  <div class="tip" style="left:8px;right:16px;top:604px;height:70px;background:var(--yellow-bg);border:1px solid var(--yellow-line);color:#c2410c">
    <svg width="12" height="14" viewBox="0 0 12 14"><circle cx="6" cy="5" r="4.5" fill="#f59e0b"/><rect x="4" y="10" width="4" height="3" rx="1" fill="#f59e0b"/></svg>
    <b style="color:#92400e">Photo Tips</b>• Use natural lighting when possible<br>• Show the final dish, not ingredients
  </div>
  <div class="btn ghost" style="left:8px;top:686px;width:136px">Skip for now</div>
  <div class="btn primary" style="left:154px;top:686px;width:136px">Continue
    <svg width="14" height="12" viewBox="0 0 14 12"><path d="M1 6h11M7.5 1.5L12 6l-4.5 4.5" stroke="#fff" stroke-width="1.8" fill="none" stroke-linecap="round" stroke-linejoin="round"/></svg></div>
</section>

<!-- Screen 3: servings -->
<section class="screen" style="left:891px;height:853px">
  <div class="hdr"><div class="track"><i style="width:50%"></i></div><div class="step-label">Step 3 of 6</div></div>
  <div class="icon-circle" style="top:90px;background:linear-gradient(135deg,#f97316,#ef4444)">
    <svg width="24" height="18" viewBox="0 0 24 18" fill="#fff"><circle cx="12" cy="5" r="3.5"/><circle cx="5" cy="7" r="2.5"/><circle cx="19" cy="7" r="2.5"/><path d="M6 16a6 6 0 0112 0z"/><path d="M0 16a5 4 0 018-2.5V16zM24 16a5 4 0 00-8-2.5V16z"/></svg>
  </div>
  <h1 class="title" style="top:172px">How Many Hungry Souls?</h1>
  <p class="sub" style="top:206px">Tell us how many people this delicious recipe will feed</p>
  <div class="abs" style="top:268px;width:100%;text-align:center;font-size:54px;font-weight:800;line-height:60px">4</div>
  <div class="abs" style="top:332px;width:100%;text-align:center;font-size:16px;color:var(--muted)">people</div>
  <div class="abs" style="left:10px;top:382px;width:26px;height:52px;border-radius:10px;background:var(--red);display:flex;align-items:center;justify-content:center"><svg width="12" height="2"><rect width="12" height="2" fill="#fff"/></svg></div>
  <div class="abs" style="left:268px;top:382px;width:26px;height:52px;border-radius:10px;background:var(--green);display:flex;align-items:center;justify-content:center"><svg width="12" height="12"><path d="M6 0v12M0 6h12" stroke="#fff" stroke-width="2"/></svg></div>
  <svg class="abs" style="left:60px;top:400px" width="190" height="16" viewBox="0 0 190 16">
    <g fill="#d1d5db"><circle cx="8" cy="8" r="4.5"/><circle cx="32" cy="8" r="4.5"/><circle cx="56" cy="8" r="4.5"/><circle cx="106" cy="8" r="4.5"/><circle cx="130" cy="8" r="4.5"/><circle cx="154" cy="8" r="4.5"/><circle cx="178" cy="8" r="4.5"/></g>
    <circle cx="81" cy="8" r="6.5" fill="#667eea"/></svg>
  <div class="chip" style="left:10px;top:462px;width:64px;height:86px;text-align:center;font-weight:500;color:#777">
    <svg style="margin-top:16px" width="18" height="20" viewBox="0 0 18 20" fill="#4b5160"><circle cx="9" cy="5" r="4.5"/><path d="M1 20a8 7 0 0116 0z"/></svg>
    <div style="font-size:11px;color:#333;margin-top:2px">1</div><div style="font-size:10px">Solo</div></div>
  <div class="chip" style="left:84px;top:462px;width:64px;height:86px;text-align:center;font-weight:500;color:#777">
    <svg style="margin-top:16px" width="20" height="18" viewBox="0 0 20 18"><path d="M10 17L2 9a4.5 4.5 0 018-5 4.5 4.5 0 018 5z" fill="#4b5160"/></svg>
    <div style="font-size:11px;color:#333;margin-top:2px">2</div><div style="font-size:10px">Couple</div></div>
  <div class="abs" style="left:157px;top:462px;width:64px;height:86px;border-radius:10px;background:#667eea"></div>
  <div class="chip" style="left:231px;top:462px;width:64px;height:86px;text-align:center;font-weight:500;color:#777">
    <svg style="margin-top:16px" width="24" height="18" viewBox="0 0 24 18" fill="#4b5160"><circle cx="8" cy="5" r="4"/><circle cx="17" cy="5" r="3.5"/><path d="M0 18a8 7 0 0116 0z"/><path d="M17 11a7 6 0 017 7h-6a9 8 0 00-3-6z"/></svg>
    <div style="font-size:11px;color:#333;margin-top:2px">8</div><div style="font-size:10px">Party</div></div>
  <div class="tip blue" style="left:10px;right:10px;top:576px;height:75px;padding-left:38px;padding-top:14px">
    <svg width="14" height="14" viewBox="0 0 14 14" style="top:20px"><circle cx="7" cy="7" r="6.5" fill="#3b82f6"/><rect x="6.2" y="6" width="1.6" height="4.5" fill="#fff"/><circle cx="7" cy="4" r="1" fill="#fff"/></svg>
    <b>Perfect Portions</b>Don't worry, people can easily scale your recipe up or down based on their needs!
  </div>
  <div class="note yellow" style="left:10px;right:10px;top:678px;height:80px">
    <svg width="24" height="24" viewBox="0 0 24 24" fill="none" stroke="#333" stroke-width="1.6"><rect x="5" y="5" width="14" height="14" rx="7"/><path d="M2 3v18M22 3v18M2 8h3M19 8h3"/></svg>
    Your recipe will serve <span class="hi-orange">4 people</span></div>
  <div class="divider" style="top:776px"></div>
  <div class="btn ghost" style="left:10px;top:795px;width:136px;height:50px;font-size:16px">Back</div>
  <div class="btn primary" style="left:157px;top:795px;width:137px;height:50px;font-size:16px">Continue
    <svg width="14" height="12" viewBox="0 0 14 12"><path d="M1 6h11M7.5 1.5L12 6l-4.5 4.5" stroke="#fff" stroke-width="1.8" fill="none" stroke-linecap="round" stroke-linejoin="round"/></svg></div>
</section>

<!-- Screen 4: ingredients -->
<section class="screen" style="left:1277px;height:918px">
  <div class="hdr" style="height:70px"><div class="track"><i style="width:66%"></i></div><div class="step-label" style="top:42px">Step 4 of 6</div></div>
  <div class="icon-circle" style="top:88px;background:linear-gradient(135deg,#22c55e,#16a34a)">
    <svg width="20" height="20" viewBox="0 0 20 20" fill="#fff"><path d="M3 17L11 6l3 3z"/><path d="M13 6l2-4M14 7l4-2M12.5 5l-.5-3" stroke="#fff" stroke-width="1.6"/></svg>
  </div>
  <h1 class="title" style="top:168px">What's in the Mix?</h1>
  <p class="sub" style="top:201px">Add all the amazing ingredients for your recipe</p>
  <div class="tip blue" style="left:14px;right:16px;top:268px;height:74px;padding-top:14px">
    <svg width="12" height="14" viewBox="0 0 12 14" style="top:30px"><circle cx="6" cy="5" r="4.5" fill="#3b82f6"/><rect x="4" y="10" width="4" height="3" rx="1" fill="#3b82f6"/></svg>
    <b>Pro Tip</b>List ingredients in the order you'll use them in your recipe!
  </div>
  <div class="card" style="left:14px;top:361px;height:60px">
    <div class="num" style="left:14px;top:17px;background:var(--orange)">1</div>
    <div class="input" style="left:50px;top:14px;width:55px;height:31px">Flour</div>
    <div class="input" style="left:112px;top:14px;width:55px;height:31px">2</div>
    <div class="input" style="left:173px;top:14px;width:55px;height:31px;justify-content:space-between">cup<svg width="8" height="5"><path d="M0 0l4 5 4-5" fill="#333"/></svg></div>
    <svg class="abs" style="left:245px;top:24px" width="9" height="11" viewBox="0 0 9 11" fill="#ef4444"><rect y="1" width="9" height="1.5"/><rect x="3" width="3" height="1.5"/><path d="M1 3h7l-.6 8H1.6z"/></svg>
  </div>
  <div class="card" style="left:14px;top:433px;height:60px">
    <div class="num" style="left:14px;top:17px;background:var(--green)">2</div>
    <div class="input" style="left:50px;top:14px;width:55px;height:31px">Sugar</div>
    <div class="input" style="left:112px;top:14px;width:55px;height:31px">1</div>
    <div class="input" style="left:173px;top:14px;width:55px;height:31px;justify-content:space-between">cup<svg width="8" height="5"><path d="M0 0l4 5 4-5" fill="#333"/></svg></div>
    <svg class="abs" style="left:245px;top:24px" width="9" height="11" viewBox="0 0 9 11" fill="#ef4444"><rect y="1" width="9" height="1.5"/><rect x="3" width="3" height="1.5"/><path d="M1 3h7l-.6 8H1.6z"/></svg>
  </div>
  <div class="card" style="left:14px;top:505px;height:60px">
    <div class="num" style="left:14px;top:17px;background:#5b7cf0">3</div>
    <div class="input" style="left:50px;top:14px;width:55px;height:31px">Eggs</div>
    <div class="input" style="left:112px;top:14px;width:55px;height:31px">3</div>
    <div class="input" style="left:173px;top:14px;width:55px;height:31px;justify-content:space-between">pie<svg width="8" height="5"><path d="M0 0l4 5 4-5" fill="#333"/></svg></div>
    <svg class="abs" style="left:245px;top:24px" width="9" height="11" viewBox="0 0 9 11" fill="#ef4444"><rect y="1" width="9" height="1.5"/><rect x="3" width="3" height="1.5"/><path d="M1 3h7l-.6 8H1.6z"/></svg>
  </div>
  <div class="btn primary" style="left:14px;right:16px;top:587px;height:48px">
    <svg width="12" height="12"><path d="M6 0v12M0 6h12" stroke="#fff" stroke-width="2"/></svg>Add Another Ingredient</div>
  <div class="chip" style="left:14px;top:656px;width:85px;height:64px;text-align:center"><div style="margin-top:40px">Salt</div></div>
  <div class="chip" style="left:109px;top:656px;width:85px;height:64px;text-align:center"><div style="margin-top:40px">Butter</div></div>
  <div class="chip" style="left:204px;top:656px;width:85px;height:64px;text-align:center"><div style="margin-top:40px">Milk</div></div>
  <div class="note yellow" style="left:14px;right:16px;top:741px;height:77px">
    <svg width="22" height="22" viewBox="0 0 22 22" fill="none" stroke="#333" stroke-width="1.5"><rect x="3" y="3" width="14" height="17" rx="1"/><path d="M6 8h8M6 12h6M12 18l8-8-2-2-8 8z"/></svg>
    You have <span class="hi-orange">3 ingredients</span> so far</div>
  <div class="divider" style="top:835px"></div>
  <div class="btn ghost" style="left:14px;top:855px;width:132px;height:49px;font-size:16px">Back</div>
  <div class="btn primary" style="left:157px;top:855px;width:132px;height:49px;font-size:16px">Continue
    <svg width="14" height="12" viewBox="0 0 14 12"><path d="M1 6h11M7.5 1.5L12 6l-4.5 4.5" stroke="#fff" stroke-width="1.8" fill="none" stroke-linecap="round" stroke-linejoin="round"/></svg></div>
</section>

<!-- Screen 5: steps -->
<section class="screen" style="left:1656px;height:1483px">
  <div class="hdr"><div class="track"><i style="width:83%"></i></div><div class="step-label">Step 5 of 6</div></div>
  <div class="icon-circle" style="top:92px;background:linear-gradient(135deg,#ec4899,#a855f7)">
    <svg width="20" height="18" viewBox="0 0 20 18" fill="#fff"><rect x="7" y="2" width="12" height="2"/><rect x="7" y="8" width="12" height="2"/><rect x="7" y="14" width="12" height="2"/><rect x="1" y="1" width="3" height="4"/><rect x="1" y="7" width="3" height="4"/><rect x="1" y="13" width="3" height="4"/></svg>
  </div>
  <h1 class="title" style="top:174px">Step by Step</h1>
  <p class="sub" style="top:207px">Break down your recipe into easy-to-follow steps</p>
  <div class="tip purple" style="left:10px;right:16px;top:275px;height:62px;padding-left:40px;padding-top:14px">
    <svg width="16" height="16" viewBox="0 0 16 16" style="top:22px;left:14px"><path d="M2 14L12 4" stroke="#a855f7" stroke-width="2"/><path d="M11 1v3M13 3h3M14 7v2M6 1v2" stroke="#a855f7" stroke-width="1.3"/></svg>
    <b style="color:#7e22ce">Magic Tip</b>Add photos to make your steps crystal clear!
  </div>
  <div class="card" style="left:10px;top:359px;height:251px">
    <div class="num" style="left:14px;top:18px;width:32px;height:32px;background:#f0507a">1</div>
    <div class="input" style="left:62px;top:13px;width:170px;height:73px;align-items:flex-start;padding:12px 14px;font-size:12px;line-height:17px;overflow:hidden">Preheat your oven to 350°F (175°C) and grease a 9-inch round cake pan with butter.</div>
    <svg class="abs" style="left:250px;top:26px" width="9" height="11" viewBox="0 0 9 11" fill="#ef4444"><rect y="1" width="9" height="1.5"/><rect x="3" width="3" height="1.5"/><path d="M1 3h7l-.6 8H1.6z"/></svg>
    <div class="photo-slot" style="left:62px;top:101px;width:170px;height:135px;padding-top:24px">
      <svg width="20" height="18" viewBox="0 0 20 18"><path d="M2 5h4l1.6-2.5h4.8L14 5h4v11H2z" fill="#9aa0ab"/><circle cx="10" cy="10" r="3" fill="#fff"/></svg>
      <div style="margin-top:6px">Add a photo for this<br>step</div><small>Tap to upload or drag &amp;<br>drop</small></div>
  </div>
  <div class="card" style="left:10px;top:626px;height:224px">
    <div class="num" style="left:14px;top:18px;width:32px;height:32px;background:#5b7cf0">2</div>
    <div class="input" style="left:62px;top:17px;width:170px;height:70px;align-items:flex-start;padding:8px 14px;font-size:12px;line-height:17px;overflow:hidden">In a large mixing bowl, cream together the butter and sugar until light and fluffy, about 3-4 minutes.</div>
    <svg class="abs" style="left:250px;top:26px" width="9" height="11" viewBox="0 0 9 11" fill="#ef4444"><rect y="1" width="9" height="1.5"/><rect x="3" width="3" height="1.5"/><path d="M1 3h7l-.6 8H1.6z"/></svg>
    <div class="media" role="img" aria-label="Step photo of butter and sugar being creamed in a bowl" style="left:62px;top:102px;width:170px;height:107px;border-radius:8px;background:radial-gradient(circle at 45% 55%,#f1d77a 0%,#e8c457 35%,#d8cfb8 70%,#eeeae2 100%)"></div>
    <div class="abs" style="left:218px;top:110px;width:20px;height:28px;border-radius:10px;background:var(--red);color:#fff;font-size:12px;display:flex;align-items:center;justify-content:center">×</div>
    <div class="abs" style="left:213px;top:181px;width:20px;height:20px;border-radius:50%;background:#fff;display:flex;align-items:center;justify-content:center"><svg width="10" height="9" viewBox="0 0 20 18"><path d="M2 5h4l1.6-2.5h4.8L14 5h4v11H2z" fill="#333"/></svg></div>
  </div>
  <div class="card" style="left:10px;top:866px;height:251px">
    <div class="num" style="left:14px;top:18px;width:32px;height:32px;background:var(--green)">3</div>
    <div class="input" style="left:62px;top:13px;width:170px;height:73px;align-items:flex-start;padding:12px 14px;font-size:12px;line-height:17px;overflow:hidden">Add eggs one at a time, beating well after each addition. Then mix in vanilla extract.</div>
    <svg class="abs" style="left:250px;top:26px" width="9" height="11" viewBox="0 0 9 11" fill="#ef4444"><rect y="1" width="9" height="1.5"/><rect x="3" width="3" height="1.5"/><path d="M1 3h7l-.6 8H1.6z"/></svg>
    <div class="photo-slot" style="left:62px;top:101px;width:170px;height:135px;padding-top:24px">
      <svg width="20" height="18" viewBox="0 0 20 18"><path d="M2 5h4l1.6-2.5h4.8L14 5h4v11H2z" fill="#9aa0ab"/><circle cx="10" cy="10" r="3" fill="#fff"/></svg>
      <div style="margin-top:6px">Add a photo for this<br>step</div><small>Tap to upload or drag &amp;<br>drop</small></div>
  </div>
  <div class="btn primary" style="left:10px;right:16px;top:1139px;height:49px;font-size:16px">
    <svg width="12" height="12"><path d="M6 0v12M0 6h12" stroke="#fff" stroke-width="2"/></svg>Add Another Step</div>
  <div class="chip" style="left:10px;top:1210px;width:136px;height:74px">
    <svg class="abs" style="left:16px;top:18px" width="18" height="18" viewBox="0 0 18 18" fill="none" stroke="#333" stroke-width="1.5"><path d="M3 3l12 12M2 6a3 3 0 014-4"/></svg>
    <div class="abs" style="left:14px;top:46px;font-size:10px">Mix dry ingredients</div></div>
  <div class="chip" style="left:157px;top:1210px;width:137px;height:74px">
    <svg class="abs" style="left:16px;top:16px" width="14" height="18" viewBox="0 0 14 18"><path d="M7 1c1 4 6 6 6 11a6 6 0 01-12 0c0-3 2-4 3-6 1 2 2 2 2 2s-1-4 1-7z" fill="#f97316" stroke="#b91c1c" stroke-width=".8"/></svg>
    <div class="abs" style="left:14px;top:46px;font-size:10px">Bake until golden</div></div>
  <div class="note green" style="left:10px;right:16px;top:1305px;height:78px">
    <svg width="20" height="24" viewBox="0 0 20 24" fill="none" stroke="#333" stroke-width="1.5"><rect x="2" y="4" width="16" height="19" rx="1"/><rect x="6" y="1" width="8" height="5" rx="1" fill="#fff"/><path d="M6 11h8M6 15h8M6 19h5"/></svg>
    You have <span class="hi-green">3 steps</span> in your recipe</div>
  <div class="divider" style="top:1401px"></div>
  <div class="btn ghost" style="left:10px;top:1421px;width:136px;height:50px;font-size:16px">Back</div>
  <div class="btn primary" style="left:157px;top:1421px;width:137px;height:50px;font-size:16px">Continue
    <svg width="14" height="12" viewBox="0 0 14 12"><path d="M1 6h11M7.5 1.5L12 6l-4.5 4.5" stroke="#fff" stroke-width="1.8" fill="none" stroke-linecap="round" stroke-linejoin="round"/></svg></div>
</section>

</div>
</body>
</html>
```